I need a new business card design for my pharmacy.

I need a business card design. I will include my logo.
The card needs to be readable. I prefer to have my logo on one side along with my website, the other side includes the other information. Please use combination of black, neon green, white, and silver. This needs to catch the eye but yet be clearly visible and legible. Thanks

Industry/Entity Type

Pharmacy

Contact Information for Business Card

It needs to have the following information listed:
Mel's Apothecary Owner/Pharm D.
7134 North Brook Lane
Sioux Falls, SD 57231
Phone 605-318-6207
Fax 605-318-6209
email: mel@melsapothecary-example.com
www.melsapothecary-example.com
Store hours Monday-Friday 8 am- 7 pm
Saturday 8 am- 12 pm
Sunday Closed
Please utilize the colors black, white, and neon green, maybe silver.

Requirements
Must have
• It needs to be easily readable!
Nice to have
• It should catch the eye.
Should not have
• Do not use any other colors except listed: black, neon green, white, & silver.

```html
<!DOCTYPE html>
<html lang="en">
<head>
<meta charset="utf-8">
<title>Mel's Apothecary – Business Card</title>
<link href="https://fonts.googleapis.com/css2?family=Montserrat:wght@600;700&family=Questrial&display=swap" rel="stylesheet">
<style>
  :root {
    --neon: #2de01a;
    --neon-deep: #1fc40f;
    --silver-light: #f2f2f2;
    --silver: #d4d4d4;
    --silver-dark: #b8b8b8;
    --ink: #111111;
    --grey-text: #555555;
    --white: #ffffff;
    --backdrop: #ecebe6;
  }
  * { box-sizing: border-box; margin: 0; padding: 0; }
  html, body { width: 1200px; height: 1000px; overflow: hidden; }
  body {
    background: var(--backdrop);
    font-family: "Questrial", "Century Gothic", sans-serif;
    position: relative;
  }
  .card {
    position: absolute;
    width: 680px;
    height: 390px;
    overflow: hidden;
    box-shadow: 0 6px 18px rgba(0,0,0,.25);
  }
  .stripes {
    background:
      repeating-linear-gradient(180deg, rgba(255,255,255,.45) 0 2px, transparent 2px 7px);
  }
  .silver-band {
    background: linear-gradient(100deg, var(--silver) 0%, var(--silver-light) 45%, var(--silver) 70%, var(--silver-light) 100%);
  }

  /* Front */
  .card-front { left: 80px; top: 70px; background: linear-gradient(135deg, var(--neon) 0%, var(--neon-deep) 100%); }
  .card-front .side-panel {
    position: absolute; left: 0; top: 0; width: 235px; height: 290px;
    background-color: var(--neon-deep);
  }
  .card-front .bottom-band { position: absolute; left: 0; bottom: 0; width: 100%; height: 100px; }
  .card-front .bottom-band.stripes-overlay {
    width: 235px;
    background: repeating-linear-gradient(180deg, rgba(0,0,0,.06) 0 2px, transparent 2px 7px);
  }
  .brand-mark {
    position: absolute; left: 30px; top: 120px; width: 180px;
    display: flex; align-items: center; gap: 10px;
    color: var(--ink); font-family: "Montserrat", sans-serif; font-weight: 700; font-size: 15px; line-height: 1.15;
  }
  .brand-mark .dot { width: 40px; height: 40px; border-radius: 50%; background: var(--ink); flex: none; }
  .divider { position: absolute; left: 232px; top: 120px; width: 3px; height: 95px; background: var(--ink); }
  .front-name {
    position: absolute; left: 255px; top: 118px;
    font-family: "Montserrat", sans-serif; font-weight: 700; font-size: 44px; color: var(--ink); letter-spacing: -.5px;
  }
  .front-url {
    position: absolute; left: 255px; top: 222px;
    font-family: "Montserrat", sans-serif; font-weight: 700; font-size: 22px; color: var(--white);
  }

  /* Back */
  .card-back { left: 440px; top: 500px; }
  .card-back .middle { position: absolute; left: 0; top: 0; width: 100%; height: 100%; }
  .card-back .top-band {
    position: absolute; left: 0; top: 0; width: 490px; height: 92px; background: var(--neon);
  }
  .card-back .top-stripes {
    position: absolute; left: 490px; top: 0; width: 190px; height: 92px; background-color: var(--neon-deep);
  }
  .card-back .bottom-band {
    position: absolute; left: 0; top: 295px; width: 100%; height: 95px; background: var(--neon);
  }
  .card-back .bottom-stripes {
    position: absolute; left: 470px; top: 245px; width: 210px; height: 145px; background-color: var(--neon-deep);
  }
  .back-title {
    position: absolute; left: 30px; top: 32px; font-size: 29px; color: var(--ink);
  }
  .info { position: absolute; display: flex; align-items: center; gap: 12px; color: var(--grey-text); font-size: 18px; line-height: 1.2; }
  .info svg { width: 22px; height: 22px; fill: var(--ink); flex: none; }
  .info.address { left: 30px; top: 120px; }
  .info.phone { left: 30px; top: 198px; }
  .info.fax { left: 30px; top: 240px; }
  .info.web { left: 340px; top: 110px; font-size: 16px; }
  .info.mail { left: 340px; top: 145px; font-size: 16px; }
  .back-brand {
    position: absolute; left: 345px; top: 195px; display: flex; align-items: center; gap: 10px;
    font-family: "Montserrat", sans-serif; font-weight: 700; font-size: 19px; color: #8f8f8f;
  }
  .back-brand .dot { width: 26px; height: 26px; border-radius: 50%; background: #a8a8a8; }
  .hours { position: absolute; left: 30px; top: 310px; font-size: 16px; color: var(--ink); line-height: 1.55; }
  .hours .day { color: #3a3a3a; }
  .hours .time { color: var(--white); }
  .hours-sat { position: absolute; left: 330px; top: 310px; font-size: 16px; }
  .hours-sat .day { color: #3a3a3a; }
  .hours-sat .time { color: var(--white); }
</style>
</head>
<body>

  <section class="card card-front" aria-label="Card front">
    <div class="side-panel stripes"></div>
    <div class="bottom-band silver-band"></div>
    <div class="bottom-band stripes-overlay"></div>
    <div class="brand-mark"><span class="dot"></span><span>Mel's<br>Apothecary</span></div>
    <div class="divider"></div>
    <h1 class="front-name">Mel's Apothecary</h1>
    <p class="front-url">www.melsapothecary-example.com</p>
  </section>

  <section class="card card-back" aria-label="Card back">
    <div class="middle silver-band"></div>
    <div class="top-band"></div>
    <div class="top-stripes stripes"></div>
    <div class="bottom-band"></div>
    <div class="bottom-stripes stripes"></div>

    <h2 class="back-title">Mel's Apothecary Owner/Pharm D</h2>

    <div class="info address">
      <svg viewBox="0 0 24 24"><path d="M12 3 2 12h3v9h5v-6h4v6h5v-9h3z"/></svg>
      <span>7134 North Brook Lane<br>Sioux Falls, SD 57231</span>
    </div>
    <div class="info phone">
      <svg viewBox="0 0 24 24"><path d="M6.6 10.8a15 15 0 0 0 6.6 6.6l2.2-2.2c.3-.3.7-.4 1-.2 1.1.4 2.3.6 3.6.6.6 0 1 .4 1 1V20c0 .6-.4 1-1 1A17 17 0 0 1 3 4c0-.6.4-1 1-1h3.5c.6 0 1 .4 1 1 0 1.3.2 2.5.6 3.6.1.3 0 .7-.2 1z"/></svg>
      <span>605-318-6207</span>
    </div>
    <div class="info fax">
      <svg viewBox="0 0 24 24"><path d="M3 7h4v14H3zM9 3h8v5H9zM8 9h13v12H8zm3 3v2h2v-2zm4 0v2h2v-2zm-4 4v2h2v-2zm4 0v2h2v-2z"/></svg>
      <span>605-318-6209</span>
    </div>
    <div class="info web">
      <svg viewBox="0 0 24 24"><circle cx="12" cy="12" r="10"/><path d="M2 12h20M12 2c3 3 3 17 0 20M12 2c-3 3-3 17 0 20" stroke="#d4d4d4" stroke-width="1.3" fill="none"/></svg>
      <span>www.melsapothecary-example.com</span>
    </div>
    <div class="info mail">
      <svg viewBox="0 0 24 24"><rect x="2" y="4" width="20" height="16" rx="3"/><path d="M5 8l7 5 7-5" stroke="#d4d4d4" stroke-width="1.8" fill="none"/></svg>
      <span>mel@melsapothecary-example.com</span>
    </div>

    <div class="back-brand"><span class="dot"></span><span>Mel's Apothecary</span></div>

    <div class="hours">
      Store hours:<br>
      <span class="day">Monday-Friday</span> <span class="time">8 am - 7 pm</span><br>
      <span class="time">Sunday Closed</span>
    </div>
    <div class="hours-sat"><span class="day">Saturday</span> <span class="time">8 am - 12 pm</span></div>
  </section>

</body>
</html>
```